Dental Medical History Form - Content provided

Design a medical history form for a dental practice. Content is provided so all that is needed is the formatting to make it look great and easy to read.

"Patient Information" to include all information contained in top portion of the "Patient Medical History Form" docx file.

"Medical History" should follow the formatting and content of the "Exact Medical History" file as this is what the entry fields look like in our practice software and so we would like it to match.

1st page - Patient info, allergies, medications, antibiotics, joint replacement, pregnancy.

2nd page - Do you have, or have you had, any of the following? . . . . . . .
Updates

Project Deadline Extended Reason: Picked too short of a deadline to start (2 days) Added Monday, February 13, 2017

Target Market(s)

All ages but must be clear enough for elderly to read. Use as much space as possible to keep font size bigger yet keep to two pages

Industry/Entity Type

Dental

Font styles to use
Sans Serif

Requirements
Must have
• All content provided
• Our logo at the top (file provided)
• Century Gothic Font
• Limit to two pages

```html
<!DOCTYPE html>
<html lang="en">
<head>
<meta charset="utf-8">
<title>Medical History Form – Page 2</title>
<link href="https://fonts.googleapis.com/css2?family=Didact+Gothic&family=Questrial&family=Arimo:wght@700&display=swap" rel="stylesheet">
<style>
  :root {
    --frame: #e7dfcf;
    --paper: #f1f1f0;
    --ink: #2f2f2f;
    --label: #505050;
    --box-fill: #ffffff;
    --box-line: #c9c9c9;
    --rule: #e3e3e3;
    --row: 19.8px;
  }
  * { box-sizing: border-box; margin: 0; padding: 0; }
  html, body {
    width: 849px; height: 1200px; overflow: hidden;
    background: var(--frame);
  }
  body { position: relative; }
  .sheet {
    position: absolute; left: 13px; top: 15px;
    width: 823px; height: 1170px;
    background: var(--paper);
  }
  .form { position: absolute; left: 0; top: 0; width: 849px; height: 1200px; }

  .prompt {
    position: absolute; left: 64px; top: 69px;
    font: 700 12.2px/1 "Arimo", Arial, sans-serif;
    color: var(--ink);
  }

  .column-rule {
    position: absolute; left: 440px; top: 123px;
    width: 4px; height: 978px; background: var(--rule);
  }

  .group { position: absolute; list-style: none; }
  .group-left { left: 64px; width: 370px; }
  .group-right { left: 472px; width: 340px; }

  .group-title {
    height: var(--row); line-height: var(--row);
    font: 700 12.4px/var(--row) "Questrial", "Century Gothic", sans-serif;
    color: var(--ink); letter-spacing: 0.1px;
  }
  .q {
    position: relative; height: var(--row);
    font: 13.6px/var(--row) "Didact Gothic", "Century Gothic", sans-serif;
    color: var(--label); white-space: nowrap;
  }
  .q-tall { height: calc(var(--row) * 2); }
  .q-tall .q-label { line-height: 15px; display: block; padding-top: 4px; }
  .q-tall .opt { top: var(--row); }

  .opt { position: absolute; left: 0; top: 0; width: 0; height: var(--row); }
  .box {
    position: absolute; top: 1.5px;
    width: 22px; height: 16.5px;
    background: var(--box-fill);
    border: 1px solid var(--box-line);
    border-radius: 1px;
  }
  .opt-text { position: absolute; top: 0; }

  /* left column: box then word */
  .group-left .opt-yes .box { left: 238px; }
  .group-left .opt-yes .opt-text { left: 266px; }
  .group-left .opt-no .box { left: 309px; }
  .group-left .opt-no .opt-text { left: 338px; }

  /* right column: word then box */
  .group-right .opt-yes .opt-text { left: 214px; }
  .group-right .opt-yes .box { left: 237px; }
  .group-right .opt-no .opt-text { left: 272px; }
  .group-right .opt-no .box { left: 294px; }

  .field {
    position: absolute; left: 472px; width: 331px;
    background: var(--box-fill); border: 1px solid var(--box-line);
  }
  .field-label {
    font: 700 13.2px/1 "Arimo", Arial, sans-serif; color: var(--ink);
    position: absolute; left: 7px;
  }

  .closing {
    position: absolute; left: 64px; top: 1001px; width: 340px;
    font: 700 13.6px/17.2px "Arimo", Arial, sans-serif; color: var(--ink);
  }
  .closing p + p { margin-top: 20px; }
</style>
</head>
<body>
<div class="sheet"></div>
<main class="form">
  <h1 class="prompt">Do you have, or have you had, any of the following ?</h1>
  <div class="column-rule"></div>

  <ul class="group group-left" style="top:106px">
    <li class="group-title">DENTAL</li>
    <li class="q"><span class="q-label">Acid Reflux</span><span class="opt opt-yes"><i class="box"></i><span class="opt-text">Yes</span></span><span class="opt opt-no"><i class="box"></i><span class="opt-text">No</span></span></li>
    <li class="q"><span class="q-label">Bad Breath/Taste</span><span class="opt opt-yes"><i class="box"></i><span class="opt-text">Yes</span></span><span class="opt opt-no"><i class="box"></i><span class="opt-text">No</span></span></li>
    <li class="q"><span class="q-label">Bleeding/Swollen/Sore Gums</span><span class="opt opt-yes"><i class="box"></i><span class="opt-text">Yes</span></span><span class="opt opt-no"><i class="box"></i><span class="opt-text">No</span></span></li>
    <li class="q"><span class="q-label">Blisters/Ulcers in Mouth</span><span class="opt opt-yes"><i class="box"></i><span class="opt-text">Yes</span></span><span class="opt opt-no"><i class="box"></i><span class="opt-text">No</span></span></li>
    <li class="q"><span class="q-label">Broken tooth/filling</span><span class="opt opt-yes"><i class="box"></i><span class="opt-text">Yes</span></span><span class="opt opt-no"><i class="box"></i><span class="opt-text">No</span></span></li>
    <li class="q"><span class="q-label">Burning tongue</span><span class="opt opt-yes"><i class="box"></i><span class="opt-text">Yes</span></span><span class="opt opt-no"><i class="box"></i><span class="opt-text">No</span></span></li>
    <li class="q"><span class="q-label">Dry mouth</span><span class="opt opt-yes"><i class="box"></i><span class="opt-text">Yes</span></span><span class="opt opt-no"><i class="box"></i><span class="opt-text">No</span></span></li>
    <li class="q"><span class="q-label">Food collection between teeth</span><span class="opt opt-yes"><i class="box"></i><span class="opt-text">Yes</span></span><span class="opt opt-no"><i class="box"></i><span class="opt-text">No</span></span></li>
    <li class="q"><span class="q-label">Grinding/clenching teeth (day/night)</span><span class="opt opt-yes"><i class="box"></i><span class="opt-text">Yes</span></span><span class="opt opt-no"><i class="box"></i><span class="opt-text">No</span></span></li>
    <li class="q"><span class="q-label">Loose teeth</span><span class="opt opt-yes"><i class="box"></i><span class="opt-text">Yes</span></span><span class="opt opt-no"><i class="box"></i><span class="opt-text">No</span></span></li>
    <li class="q"><span class="q-label">Crooked teeth</span><span class="opt opt-yes"><i class="box"></i><span class="opt-text">Yes</span></span><span class="opt opt-no"><i class="box"></i><span class="opt-text">No</span></span></li>
    <li class="q"><span class="q-label">Discoloured teeth</span><span class="opt opt-yes"><i class="box"></i><span class="opt-text">Yes</span></span><span class="opt opt-no"><i class="box"></i><span class="opt-text">No</span></span></li>
    <li class="q"><span class="q-label">Sensitivity to Hot/Cold</span><span class="opt opt-yes"><i class="box"></i><span class="opt-text">Yes</span></span><span class="opt opt-no"><i class="box"></i><span class="opt-text">No</span></span></li>
    <li class="q"><span class="q-label">Tooth pain when chewing</span><span class="opt opt-yes"><i class="box"></i><span class="opt-text">Yes</span></span><span class="opt opt-no"><i class="box"></i><span class="opt-text">No</span></span></li>
    <li class="q"><span class="q-label">Jaw pain/Fracture</span><span class="opt opt-yes"><i class="box"></i><span class="opt-text">Yes</span></span><span class="opt opt-no"><i class="box"></i><span class="opt-text">No</span></span></li>
    <li class="q"><span class="q-label">Orthodontic treatment/history</span><span class="opt opt-yes"><i class="box"></i><span class="opt-text">Yes</span></span><span class="opt opt-no"><i class="box"></i><span class="opt-text">No</span></span></li>
    <li class="q"><span class="q-label">Oral Cancer</span><span class="opt opt-yes"><i class="box"></i><span class="opt-text">Yes</span></span><span class="opt opt-no"><i class="box"></i><span class="opt-text">No</span></span></li>
  </ul>

  <ul class="group group-left" style="top:481px">
    <li class="group-title">DIET/LIFESTYLE</li>
    <li class="q q-tall"><span class="q-label">Drink more than 1glass<br>alcohol per day</span><span class="opt opt-yes"><i class="box"></i><span class="opt-text">Yes</span></span><span class="opt opt-no"><i class="box"></i><span class="opt-text">No</span></span></li>
    <li class="q"><span class="q-label">Smoking</span><span class="opt opt-yes"><i class="box"></i><span class="opt-text">Yes</span></span><span class="opt opt-no"><i class="box"></i><span class="opt-text">No</span></span></li>
    <li class="q"><span class="q-label">Carbonated drinks</span><span class="opt opt-yes"><i class="box"></i><span class="opt-text">Yes</span></span><span class="opt opt-no"><i class="box"></i><span class="opt-text">No</span></span></li>
    <li class="q"><span class="q-label">Sugary foods</span><span class="opt opt-yes"><i class="box"></i><span class="opt-text">Yes</span></span><span class="opt opt-no"><i class="box"></i><span class="opt-text">No</span></span></li>
  </ul>

  <ul class="group group-left" style="top:615px">
    <li class="group-title">BLOOD</li>
    <li class="q"><span class="q-label">Anaemia</span><span class="opt opt-yes"><i class="box"></i><span class="opt-text">Yes</span></span><span class="opt opt-no"><i class="box"></i><span class="opt-text">No</span></span></li>
    <li class="q"><span class="q-label">Blood clots</span><span class="opt opt-yes"><i class="box"></i><span class="opt-text">Yes</span></span><span class="opt opt-no"><i class="box"></i><span class="opt-text">No</span></span></li>
    <li class="q"><span class="q-label">Leukemia</span><span class="opt opt-yes"><i class="box"></i><span class="opt-text">Yes</span></span><span class="opt opt-no"><i class="box"></i><span class="opt-text">No</span></span></li>
    <li class="q"><span class="q-label">Low platelets</span><span class="opt opt-yes"><i class="box"></i><span class="opt-text">Yes</span></span><span class="opt opt-no"><i class="box"></i><span class="opt-text">No</span></span></li>
    <li class="q"><span class="q-label">Lymphoma</span><span class="opt opt-yes"><i class="box"></i><span class="opt-text">Yes</span></span><span class="opt opt-no"><i class="box"></i><span class="opt-text">No</span></span></li>
  </ul>

  <ul class="group group-left" style="top:754px">
    <li class="group-title">CHEST</li>
    <li class="q"><span class="q-label">Bronchitis</span><span class="opt opt-yes"><i class="box"></i><span class="opt-text">Yes</span></span><span class="opt opt-no"><i class="box"></i><span class="opt-text">No</span></span></li>
    <li class="q"><span class="q-label">Cystic Fibrosis</span><span class="opt opt-yes"><i class="box"></i><span class="opt-text">Yes</span></span><span class="opt opt-no"><i class="box"></i><span class="opt-text">No</span></span></li>
    <li class="q"><span class="q-label">Emphysema</span><span class="opt opt-yes"><i class="box"></i><span class="opt-text">Yes</span></span><span class="opt opt-no"><i class="box"></i><span class="opt-text">No</span></span></li>
    <li class="q"><span class="q-label">Pneumonia</span><span class="opt opt-yes"><i class="box"></i><span class="opt-text">Yes</span></span><span class="opt opt-no"><i class="box"></i><span class="opt-text">No</span></span></li>
  </ul>

  <ul class="group group-left" style="top:873px">
    <li class="group-title">INFECTIOUS DISEASE</li>
    <li class="q"><span class="q-label">Creutzfeldt-Jakob Disease</span><span class="opt opt-yes"><i class="box"></i><span class="opt-text">Yes</span></span><span class="opt opt-no"><i class="box"></i><span class="opt-text">No</span></span></li>
    <li class="q"><span class="q-label">Hepatitis A,B,C,D</span><span class="opt opt-yes"><i class="box"></i><span class="opt-text">Yes</span></span><span class="opt opt-no"><i class="box"></i><span class="opt-text">No</span></span></li>
    <li class="q"><span class="q-label">HIV/AIDS</span><span class="opt opt-yes"><i class="box"></i><span class="opt-text">Yes</span></span><span class="opt opt-no"><i class="box"></i><span class="opt-text">No</span></span></li>
  </ul>

  <section class="closing">
    <p>Thank you for the time to complete<br>your medical history form.</p>
    <p>Oral health is linked to overall health and<br>this comprehensive questionnaire will help us to<br>provide you with optimal and safe care.</p>
  </section>

  <ul class="group group-right" style="top:124px">
    <li class="q"><span class="q-label">Influenza</span><span class="opt opt-yes"><span class="opt-text">Yes</span><i class="box"></i></span><span class="opt opt-no"><span class="opt-text">No</span><i class="box"></i></span></li>
    <li class="q"><span class="q-label">Shingles</span><span class="opt opt-yes"><span class="opt-text">Yes</span><i class="box"></i></span><span class="opt opt-no"><span class="opt-text">No</span><i class="box"></i></span></li>
    <li class="q"><span class="q-label">Tuberculosis</span><span class="opt opt-yes"><span class="opt-text">Yes</span><i class="box"></i></span><span class="opt opt-no"><span class="opt-text">No</span><i class="box"></i></span></li>
  </ul>

  <ul class="group group-right" style="top:204px">
    <li class="group-title">HEART</li>
    <li class="q"><span class="q-label">Angina</span><span class="opt opt-yes"><span class="opt-text">Yes</span><i class="box"></i></span><span class="opt opt-no"><span class="opt-text">No</span><i class="box"></i></span></li>
    <li class="q"><span class="q-label">Atrial Fibrillation</span><span class="opt opt-yes"><span class="opt-text">Yes</span><i class="box"></i></span><span class="opt opt-no"><span class="opt-text">No</span><i class="box"></i></span></li>
    <li class="q"><span class="q-label">Blood Pressure (High/Low)</span><span class="opt opt-yes"><span class="opt-text">Yes</span><i class="box"></i></span><span class="opt opt-no"><span class="opt-text">No</span><i class="box"></i></span></li>
    <li class="q"><span class="q-label">Congenital Heart Disease</span><span class="opt opt-yes"><span class="opt-text">Yes</span><i class="box"></i></span><span class="opt opt-no"><span class="opt-text">No</span><i class="box"></i></span></li>
    <li class="q"><span class="q-label">Heart attack</span><span class="opt opt-yes"><span class="opt-text">Yes</span><i class="box"></i></span><span class="opt opt-no"><span class="opt-text">No</span><i class="box"></i></span></li>
    <li class="q"><span class="q-label">Heart murmur</span><span class="opt opt-yes"><span class="opt-text">Yes</span><i class="box"></i></span><span class="opt opt-no"><span class="opt-text">No</span><i class="box"></i></span></li>
    <li class="q"><span class="q-label">Heart surgery</span><span class="opt opt-yes"><span class="opt-text">Yes</span><i class="box"></i></span><span class="opt opt-no"><span class="opt-text">No</span><i class="box"></i></span></li>
    <li class="q"><span class="q-label">Heart valve replacement</span><span class="opt opt-yes"><span class="opt-text">Yes</span><i class="box"></i></span><span class="opt opt-no"><span class="opt-text">No</span><i class="box"></i></span></li>
    <li class="q"><span class="q-label">Infective endocarditis</span><span class="opt opt-yes"><span class="opt-text">Yes</span><i class="box"></i></span><span class="opt opt-no"><span class="opt-text">No</span><i class="box"></i></span></li>
    <li class="q"><span class="q-label">Rheumatic Heart Disease</span><span class="opt opt-yes"><span class="opt-text">Yes</span><i class="box"></i></span><span class="opt opt-no"><span class="opt-text">No</span><i class="box"></i></span></li>
    <li class="q"><span class="q-label">Pacemaker</span><span class="opt opt-yes"><span class="opt-text">Yes</span><i class="box"></i></span><span class="opt opt-no"><span class="opt-text">No</span><i class="box"></i></span></li>
    <li class="q"><span class="q-label">Stent</span><span class="opt opt-yes"><span class="opt-text">Yes</span><i class="box"></i></span><span class="opt opt-no"><span class="opt-text">No</span><i class="box"></i></span></li>
  </ul>

  <ul class="group group-right" style="top:483px">
    <li class="group-title">OTHER</li>
    <li class="q"><span class="q-label">Anxiety/PTSD</span><span class="opt opt-yes"><span class="opt-text">Yes</span><i class="box"></i></span><span class="opt opt-no"><span class="opt-text">No</span><i class="box"></i></span></li>
    <li class="q"><span class="q-label">Arthritis</span><span class="opt opt-yes"><span class="opt-text">Yes</span><i class="box"></i></span><span class="opt opt-no"><span class="opt-text">No</span><i class="box"></i></span></li>
    <li class="q"><span class="q-label">Alzheimer's</span><span class="opt opt-yes"><span class="opt-text">Yes</span><i class="box"></i></span><span class="opt opt-no"><span class="opt-text">No</span><i class="box"></i></span></li>
    <li class="q"><span class="q-label">Asthma</span><span class="opt opt-yes"><span class="opt-text">Yes</span><i class="box"></i></span><span class="opt opt-no"><span class="opt-text">No</span><i class="box"></i></span></li>
    <li class="q"><span class="q-label">Anaphylaxis</span><span class="opt opt-yes"><span class="opt-text">Yes</span><i class="box"></i></span><span class="opt opt-no"><span class="opt-text">No</span><i class="box"></i></span></li>
    <li class="q"><span class="q-label">Auto-immune disease</span><span class="opt opt-yes"><span class="opt-text">Yes</span><i class="box"></i></span><span class="opt opt-no"><span class="opt-text">No</span><i class="box"></i></span></li>
    <li class="q"><span class="q-label">Coeliac</span><span class="opt opt-yes"><span class="opt-text">Yes</span><i class="box"></i></span><span class="opt opt-no"><span class="opt-text">No</span><i class="box"></i></span></li>
    <li class="q"><span class="q-label">Depression</span><span class="opt opt-yes"><span class="opt-text">Yes</span><i class="box"></i></span><span class="opt opt-no"><span class="opt-text">No</span><i class="box"></i></span></li>
    <li class="q"><span class="q-label">Diabetes</span><span class="opt opt-yes"><span class="opt-text">Yes</span><i class="box"></i></span><span class="opt opt-no"><span class="opt-text">No</span><i class="box"></i></span></li>
    <li class="q"><span class="q-label">Epilepsy</span><span class="opt opt-yes"><span class="opt-text">Yes</span><i class="box"></i></span><span class="opt opt-no"><span class="opt-text">No</span><i class="box"></i></span></li>
    <li class="q"><span class="q-label">Kidney Disease</span><span class="opt opt-yes"><span class="opt-text">Yes</span><i class="box"></i></span><span class="opt opt-no"><span class="opt-text">No</span><i class="box"></i></span></li>
    <li class="q"><span class="q-label">Liver Disease</span><span class="opt opt-yes"><span class="opt-text">Yes</span><i class="box"></i></span><span class="opt opt-no"><span class="opt-text">No</span><i class="box"></i></span></li>
    <li class="q"><span class="q-label">Osteoporosis</span><span class="opt opt-yes"><span class="opt-text">Yes</span><i class="box"></i></span><span class="opt opt-no"><span class="opt-text">No</span><i class="box"></i></span></li>
    <li class="q"><span class="q-label">Parkinson's</span><span class="opt opt-yes"><span class="opt-text">Yes</span><i class="box"></i></span><span class="opt opt-no"><span class="opt-text">No</span><i class="box"></i></span></li>
    <li class="q"><span class="q-label">Radiation to Head/Neck</span><span class="opt opt-yes"><span class="opt-text">Yes</span><i class="box"></i></span><span class="opt opt-no"><span class="opt-text">No</span><i class="box"></i></span></li>
    <li class="q"><span class="q-label">Schizophrenia</span><span class="opt opt-yes"><span class="opt-text">Yes</span><i class="box"></i></span><span class="opt opt-no"><span class="opt-text">No</span><i class="box"></i></span></li>
    <li class="q"><span class="q-label">Snoring</span><span class="opt opt-yes"><span class="opt-text">Yes</span><i class="box"></i></span><span class="opt opt-no"><span class="opt-text">No</span><i class="box"></i></span></li>
    <li class="q"><span class="q-label">Sleep apnea</span><span class="opt opt-yes"><span class="opt-text">Yes</span><i class="box"></i></span><span class="opt opt-no"><span class="opt-text">No</span><i class="box"></i></span></li>
    <li class="q"><span class="q-label">Stroke</span><span class="opt opt-yes"><span class="opt-text">Yes</span><i class="box"></i></span><span class="opt opt-no"><span class="opt-text">No</span><i class="box"></i></span></li>
  </ul>

  <ul class="group group-right" style="top:901px">
    <li class="group-title">OTHER</li>
  </ul>
  <div class="field" style="top:922px;height:23px"></div>
  <div class="field" style="top:954px;height:23px"></div>

  <div class="field" style="top:1002px;height:70px"><span class="field-label" style="top:10px">SIGNATURE</span></div>
  <div class="field" style="top:1079px;height:23px"><span class="field-label" style="top:5px">Date:</span></div>
</main>
</body>
</html>
```